Signage Design Project

We need a logo and signage for the shopfront of a personal fitness training gym and coaching facility. We want the signage to cover the glass shopfront windows which consist of 4 glass windows with dimensions: 1 of 200cm x 180cm, 2 of 180cm x 135cm and 1 of 180cm x 180cm. The windows that are 200x 180 and 180x180 are the most visable/ important. We want the 200x180 to display the logo and our name which is "Harborline Fitness Centre" with further information of: Your personal training studio and boutique coaching gym Ph: 9471 2286.
For the window with 180 x 180cm measurement we want to list the services we provide which are:
Personal Training Sessions | Group Classes|Weight Loss |Toning & Sculpting|Bodybuilding I Cardio|Weights| Kettlebells| Boxing| Circuits I Team Building Programs| Boot Camp I Healthy Lifestyle & Wellness Coaching
The 2 windows 180x135cm are diagonal to the entry of the shop. We want them to be the same and plainer in design with the words: Harborline Fitness Centre
Personal Training Studio and Boutique Coaching Gym
The signage design also includes an acrylic window box that lights up which is to display the logo and Harborline Fitness Centre

```html
<!DOCTYPE html>
<html lang="en">
<head>
<meta charset="utf-8">
<title>Harborline Fitness Centre – Shopfront Signage</title>
<link href="https://fonts.googleapis.com/css2?family=Montserrat:wght@600;700;800&family=Quicksand:wght@500;600&display=swap" rel="stylesheet">
<style>
  :root {
    --backdrop: #0b7590;
    --sign-blue-light: #12b4e8;
    --sign-blue: #0a86b8;
    --sign-blue-deep: #08638f;
    --accent-green: #a4b82a;
    --panel-white: #ffffff;
    --text-blue: #1a8fc6;
    --photo-tone-a: #c9dde6;
    --photo-tone-b: #7fb4cc;
  }
  * { box-sizing: border-box; margin: 0; padding: 0; }
  html, body { width: 1200px; height: 900px; overflow: hidden; }
  body { background: var(--backdrop); position: relative; font-family: "Quicksand", sans-serif; }

  .sign { position: absolute; background: var(--panel-white); overflow: hidden; }
  .sign-art { position: absolute; inset: 0; width: 100%; height: 100%; }

  /* Main window: 200 x 180 */
  .window-main { left: 215px; top: 115px; width: 390px; height: 330px; }
  .window-main .field { position: absolute; left: 30px; top: 20px; width: 330px; height: 290px; overflow: hidden; }
  .brand-main { position: absolute; left: 40px; top: 80px; display: flex; align-items: center; gap: 10px; }
  .brand-mark { border-radius: 50%; background: var(--panel-white); flex: none; }
  .brand-main .brand-mark { width: 44px; height: 44px; }
  .brand-name { font-family: "Montserrat", sans-serif; font-weight: 800; color: var(--panel-white); line-height: 1.05; }
  .brand-main .brand-name { font-size: 25px; }
  .tagline-main { position: absolute; left: 0; right: 0; top: 148px; text-align: center; color: var(--panel-white);
    font-size: 15px; font-weight: 500; letter-spacing: 1.3px; line-height: 16px; }
  .phone-main { position: absolute; left: 0; right: 0; top: 224px; display: flex; justify-content: center; align-items: center; gap: 6px;
    color: var(--panel-white); font-size: 22px; font-weight: 600; letter-spacing: 1px; }
  .phone-icon { width: 12px; height: 20px; }

  /* Services window: 180 x 180 */
  .window-services { left: 620px; top: 520px; width: 195px; height: 235px; }
  .brand-services { position: absolute; left: 34px; top: 18px; display: flex; align-items: center; gap: 5px; }
  .brand-services .brand-mark, .brand-side .brand-mark { background: var(--text-blue); }
  .brand-services .brand-mark { width: 20px; height: 20px; }
  .brand-services .brand-name, .brand-side .brand-name { color: var(--text-blue); }
  .brand-services .brand-name { font-size: 11px; }
  .service-list { position: absolute; left: 4px; right: 4px; top: 64px; list-style: none; text-align: center;
    font-family: "Montserrat", sans-serif; font-weight: 700; font-size: 7.3px; line-height: 16px; color: var(--text-blue); }
  .photo-services { position: absolute; left: 92px; top: 140px; width: 92px; height: 85px;
    background: linear-gradient(160deg, var(--photo-tone-a), var(--photo-tone-b)); border-radius: 4px; }

  /* Side windows: 180 x 135 */
  .window-side { left: 852px; top: 545px; width: 70px; height: 210px; }
  .brand-side { position: absolute; left: 6px; top: 34px; display: flex; align-items: center; gap: 3px; }
  .brand-side .brand-mark { width: 10px; height: 10px; }
  .brand-side .brand-name { font-size: 6.5px; }
  .tagline-side { position: absolute; left: 4px; right: 4px; top: 82px; text-align: center;
    font-family: "Montserrat", sans-serif; font-weight: 700; color: var(--accent-green); font-size: 6px; line-height: 8px; }
  .photo-side { position: absolute; left: 14px; top: 118px; width: 44px; height: 62px;
    background: linear-gradient(160deg, var(--photo-tone-a), var(--photo-tone-b)); border-radius: 3px; }
</style>
</head>
<body>

<section class="sign window-main" aria-label="Main window sign">
  <div class="field">
    <svg class="sign-art" viewBox="0 0 330 290" preserveAspectRatio="none" aria-hidden="true">
      <defs>
        <linearGradient id="mainBlue" x1="0" y1="0" x2="0.3" y2="1">
          <stop offset="0" stop-color="var(--sign-blue-light)"/>
          <stop offset="0.55" stop-color="var(--sign-blue)"/>
          <stop offset="1" stop-color="var(--sign-blue-deep)"/>
        </linearGradient>
      </defs>
      <rect width="330" height="290" fill="url(#mainBlue)"/>
      <path d="M0 0 H125 Q30 20 0 110 Z" fill="var(--accent-green)"/>
      <path d="M330 175 Q315 260 205 290 H330 Z" fill="var(--accent-green)"/>
    </svg>
    <div class="brand-main">
      <span class="brand-mark"></span>
      <span class="brand-name">Harborline<br>Fitness Centre</span>
    </div>
    <p class="tagline-main">Your personal training<br>studio &amp; boutique<br>coaching gym</p>
    <p class="phone-main">
      <svg class="phone-icon" viewBox="0 0 12 20" aria-hidden="true">
        <rect x="1" y="1" width="10" height="18" rx="2" fill="none" stroke="currentColor" stroke-width="2"/>
        <rect x="3" y="4" width="6" height="8" fill="currentColor"/>
      </svg>
      9471 2286
    </p>
  </div>
</section>

<section class="sign window-services" aria-label="Services window sign">
  <svg class="sign-art" viewBox="0 0 195 235" preserveAspectRatio="none" aria-hidden="true">
    <path d="M0 150 Q60 205 195 215 V235 H0 Z" fill="var(--accent-green)"/>
    <path d="M0 170 Q70 215 195 222 V235 H0 Z" fill="var(--panel-white)"/>
    <path d="M0 188 Q60 222 195 228 V235 H0 Z" fill="var(--sign-blue)"/>
  </svg>
  <div class="brand-services">
    <span class="brand-mark"></span>
    <span class="brand-name">Harborline<br>Fitness Centre</span>
  </div>
  <ul class="service-list">
    <li>Personal Training Sessions | Group Classes</li>
    <li>Weight Loss | Toning &amp; Sculpting | Bodybuilding</li>
    <li>Cardio | Weights | Kettlebells | Boxing | Circuits</li>
    <li>Team Building Programs | Boot Camp</li>
    <li>Healthy Lifestyle &amp; Wellness Coaching</li>
  </ul>
  <div class="photo-services" role="img" aria-label="Photo of a woman in sportswear stretching on the floor"></div>
</section>

<section class="sign window-side" aria-label="Side window sign">
  <svg class="sign-art" viewBox="0 0 70 210" preserveAspectRatio="none" aria-hidden="true">
    <path d="M0 150 Q25 190 70 195 V210 H0 Z" fill="var(--accent-green)"/>
    <path d="M0 172 Q25 200 70 203 V210 H0 Z" fill="var(--sign-blue)"/>
  </svg>
  <div class="brand-side">
    <span class="brand-mark"></span>
    <span class="brand-name">Harborline<br>Fitness Centre</span>
  </div>
  <p class="tagline-side">Personal Training<br>Studio &amp; Boutique Coaching Gym</p>
  <div class="photo-side" role="img" aria-label="Photo of a woman in sportswear stretching"></div>
</section>

</body>
</html>
```